Summit Builders Web Site / Business Cards

Construction Company that specializes in Water and Fire Damage, Residential ReModels, Landscaping and Building ADU (Accessory Dwelling Unit)

Growing and changing families often need additional space, and a remodeling project can often provide that. Adding a new area, or repurposing an existing one can satisfy this requirement.

Other times, homeowners want to update the look in their kitchen or bathroom with more than just a change of cabinetry or vanity doors and drawers. Whatever your needs are, Summit Builders has skilled workers who are bonded and insured, and ready to make your dreams and visions a reality.

Target Market(s)

Home Owners

Industry/Entity Type

Construction Company

Contact Information for Business Card

Center Logo with our information on the corners

Back side to be Logo Only
Contact Info
CSLB License # 4829516
info@summitbuildersca.example
www.summitbuildersca.example

Coding

Coded - Design and coding required

Number of Pages Required

5+ page

Font styles to use
Serif
Sans Serif

Requirements
Must have
• Using our Logo Colors
Home
About Us
Services
Projects / Portfolio
Contact Us
Nice to have
• Colors matching our Logo
Should not have
• Black because it doesnt match our logo

```html
<!DOCTYPE html>
<html lang="en">
<head>
<meta charset="utf-8">
<title>Summit Builders</title>
<link href="https://fonts.googleapis.com/css2?family=Poppins:wght@400;500;600;700&family=Open+Sans:wght@400;600&display=swap" rel="stylesheet">
<style>
:root{
  --orange:#f26522;
  --orange-dark:#e05412;
  --navy:#1d1f2c;
  --navy-2:#262938;
  --ink:#23242c;
  --muted:#8a8d97;
  --pale:#f4f6f9;
  --sky:#cfe6f5;
  --white:#ffffff;
}
*{box-sizing:border-box;margin:0;padding:0}
html,body{width:1200px;height:4744px;overflow:hidden}
body{font-family:"Open Sans",Arial,sans-serif;color:var(--ink);background:var(--white);position:relative}
h1,h2,h3,h4,.btn,.brand,.stat-num{font-family:"Poppins",Arial,sans-serif}
.btn{display:inline-block;background:var(--orange);color:var(--white);font-size:13px;font-weight:600;letter-spacing:.5px;text-transform:uppercase;padding:16px 28px;border-radius:3px}

/* Hero */
.hero{position:absolute;top:0;left:0;width:1200px;height:820px;overflow:hidden}
.hero-photo{position:absolute;inset:0;background:linear-gradient(180deg,#7fa9c4 0%,#a9c2cf 35%,#d9b98d 62%,#8a6f58 80%,#5d5a5c 100%)}
.hero-shade{position:absolute;inset:0;background:linear-gradient(90deg,rgba(20,30,50,.35),rgba(20,30,50,0) 60%)}
.nav{position:absolute;top:44px;left:128px;right:128px;display:flex;align-items:center}
.brand{display:flex;align-items:center;gap:10px;font-size:20px;font-weight:700;color:var(--white)}
.brand-mark{width:22px;height:22px;background:var(--orange)}
.nav-links{display:flex;gap:22px;margin-left:auto;margin-right:42px}
.nav-links a{color:var(--white);font-size:13px;font-family:"Poppins",sans-serif;text-decoration:none}
.nav-links a.active{color:var(--white);border-bottom:2px solid var(--orange)}
.btn-quote{background:var(--white);color:var(--orange);padding:13px 22px;font-size:12px}
.hero-copy{position:absolute;top:180px;left:128px}
.hero-copy h1{color:var(--white);font-size:52px;line-height:60px;font-weight:700}
.hero-copy .tag{color:var(--orange);font-family:"Poppins",sans-serif;font-size:22px;font-weight:500;margin:8px 0 30px;text-transform:uppercase}
.hero-cut{position:absolute;bottom:0;left:0}

/* Section headings */
.sec-title{text-align:center;font-size:40px;line-height:56px;font-weight:700;color:var(--ink)}
.sec-intro{text-align:center;color:var(--muted);font-size:15px;line-height:26px;width:640px;margin:22px auto 0}

/* Services */
.services{position:absolute;top:860px;left:0;width:1200px}
.svc-grid{display:grid;grid-template-columns:repeat(3,300px);column-gap:50px;row-gap:70px;width:1000px;margin:56px auto 0}
.svc{text-align:center}
.svc-icon{width:84px;height:84px;margin:0 auto;border-radius:50%;background:var(--white);box-shadow:0 8px 24px rgba(0,0,0,.09);display:flex;align-items:center;justify-content:center}
.svc h3{font-size:17px;line-height:24px;font-weight:600;margin:26px 0 10px}
.svc p{font-size:12px;line-height:20px;color:var(--muted)}

/* About */
.about{position:absolute;top:1530px;left:0;width:1200px;height:830px}
.about-bg{position:absolute;inset:0}
.about-copy{position:absolute;top:200px;left:128px;width:540px;color:#e6e7ec}
.about-copy h2{font-size:42px;color:var(--white);font-weight:700;margin-bottom:28px}
.about-copy p{font-size:14px;line-height:25px;color:#c9cbd3;margin-bottom:18px}
.ticks{display:grid;grid-template-columns:240px 240px;row-gap:16px;margin:26px 0 50px;list-style:none}
.ticks li{font-size:13px;display:flex;gap:10px;align-items:center;color:#e6e7ec}
.about-photo{position:absolute;top:292px;left:712px;width:360px;height:420px;background:linear-gradient(160deg,#dfe5ea 0%,#a8b6c2 45%,#6c7d8c 100%)}
.about-dots{position:absolute;top:262px;left:682px;width:120px;height:120px;background-image:radial-gradient(#4a4e60 1.5px,transparent 1.6px);background-size:12px 12px}

/* Projects */
.projects{position:absolute;top:2400px;left:0;width:1200px}
.proj-grid{display:grid;grid-template-columns:296px 300px 300px;column-gap:24px;row-gap:36px;width:944px;margin:50px auto 0}
.proj{height:262px;position:relative;display:flex;align-items:center;justify-content:center;flex-direction:column}
.proj span{color:var(--white);font-family:"Poppins",sans-serif;font-weight:500;font-size:16px}
.proj.feature{background:var(--orange)}
.proj.feature p{color:#ffe3d3;font-size:12px;line-height:19px;text-align:center;width:220px;margin-top:10px}
.p1{background:linear-gradient(160deg,#6d8f5a,#3f5f3c 60%,#7c8a86)}
.p3{background:linear-gradient(160deg,#d8cbb4,#b49c7c 60%,#8c7357)}
.p4{background:linear-gradient(160deg,#7aa4b0,#3f6e5c 55%,#2d4a3e)}
.p5{background:linear-gradient(160deg,#c9a781,#8c6a4c 55%,#4f5b4a)}
.p6{background:linear-gradient(160deg,#f0ede7,#cfc8bc 60%,#7f8b6e)}

/* Stats */
.stats{position:absolute;top:3128px;left:0;width:1200px;height:200px;background:var(--navy-2);display:flex;justify-content:center}
.stat{width:240px;text-align:center;padding-top:58px}
.stat-num{font-size:36px;font-weight:600;color:var(--orange)}
.stat-label{font-size:14px;color:var(--white);margin-top:6px}

/* Testimonials */
.testimonials{position:absolute;top:3380px;left:0;width:1200px}
.quotes{display:flex;gap:80px;width:800px;margin:68px auto 0}
.quote{width:360px}
.quote-box{background:var(--white);box-shadow:0 6px 22px rgba(0,0,0,.07);padding:26px 28px;font-size:12px;line-height:21px;color:var(--muted);height:160px}
.person{display:flex;align-items:center;gap:16px;margin:26px 0 0 10px}
.avatar{width:72px;height:72px;border-radius:50%}
.a1{background:linear-gradient(160deg,#d9c7b0,#8c7560)}
.a2{background:linear-gradient(160deg,#e6d2c8,#5e4a45)}
.person h4{font-size:14px;font-weight:500}
.person small{font-size:11px;color:var(--orange)}

/* CTA */
.cta{position:absolute;top:3968px;left:208px;width:780px;height:230px;background:var(--orange);text-align:center;color:var(--white);padding-top:48px}
.cta h2{font-size:32px;font-weight:600}
.cta p{font-size:13px;margin:10px 0 26px;color:#ffe6d8}
.cta-form{display:flex;justify-content:center}
.cta-form .field{width:420px;height:48px;background:var(--orange-dark);border:1px solid #ff8f59;color:#ffc9ab;font-size:12px;text-align:left;padding:15px 18px}
.cta-form .send{width:110px;height:48px;background:var(--white);color:var(--ink);font-family:"Poppins",sans-serif;font-weight:600;font-size:14px;line-height:48px}

/* Footer */
.footer{position:absolute;top:4260px;left:128px;width:944px}
.foot-cols{display:grid;grid-template-columns:330px 350px 264px}
.foot-brand .brand{color:var(--ink);font-size:20px}
.foot-brand p{font-size:12px;line-height:20px;color:var(--muted);margin:24px 0 20px;width:260px}
.socials{display:flex;gap:8px}
.socials i{width:26px;height:26px;border-radius:50%;background:var(--ink);display:block}
.footer h4{font-size:16px;font-weight:600;margin:16px 0 18px}
.footer .col p{font-size:12px;line-height:21px;color:#5c5f69}
.copyright{position:absolute;top:4640px;left:128px;width:944px;border-top:1px solid #e5e7ec;padding-top:22px;text-align:center;font-size:12px;color:#6b6e78}
</style>
</head>
<body>

<header class="hero">
  <div class="hero-photo" role="img" aria-label="Construction workers in safety vests on a building site at sunset, one pointing across the skyline"></div>
  <div class="hero-shade"></div>
  <nav class="nav">
    <div class="brand"><span class="brand-mark"></span>Summit Builders</div>
    <div class="nav-links">
      <a class="active">Home</a><a>About Us</a><a>Services</a><a>Project Portfolio</a><a>Contact Us</a>
    </div>
    <span class="btn btn-quote">Get a Quote</span>
  </nav>
  <div class="hero-copy">
    <h1>Welcome to<br>SUMMIT BUILDERS</h1>
    <p class="tag">The best choice us, because we do her</p>
    <span class="btn">Contact Now</span>
  </div>
  <svg class="hero-cut" width="1200" height="120" viewBox="0 0 1200 120">
    <polygon points="900,10 1200,60 1200,120 980,120" fill="var(--sky)"/>
    <polygon points="0,60 560,110 900,30 1080,120 0,120" fill="var(--white)"/>
  </svg>
</header>

<section class="services">
  <h2 class="sec-title">Discover Our Services</h2>
  <p class="sec-intro">Lorem ipsum dolor sit amet, consectetur adipiscing elit. Praesent urna sem, semper sit amet auctor in, auctor nisl leo. Curabitur aliquam sit amet turpis at.</p>
  <div class="svc-grid">
    <div class="svc">
      <div class="svc-icon"><svg width="36" height="36" viewBox="0 0 36 36" fill="none" stroke="var(--orange)" stroke-width="2"><path d="M5 17 18 6l13 11"/><path d="M9 14v16h18V14"/><rect x="15" y="21" width="6" height="9"/></svg></div>
      <h3>Home Construction</h3>
      <p>Lorem ipsum dolor sit amet consectetur adipiscing elit praesent urna sem semper sit amet auctor</p>
    </div>
    <div class="svc">
      <div class="svc-icon"><svg width="36" height="36" viewBox="0 0 36 36" fill="none" stroke="var(--orange)" stroke-width="2"><rect x="6" y="12" width="24" height="18"/><path d="M6 12 18 5l12 7"/><path d="M12 30v-9h12v9"/></svg></div>
      <h3>Building Remodeling</h3>
      <p>Lorem ipsum dolor sit amet consectetur adipiscing elit praesent urna sem semper sit amet auctor</p>
    </div>
    <div class="svc">
      <div class="svc-icon"><svg width="36" height="36" viewBox="0 0 36 36" fill="none" stroke="var(--orange)" stroke-width="2"><rect x="6" y="8" width="24" height="16"/><path d="M10 30h16M18 24v6"/><path d="M11 19l5-6 4 4 5-5"/></svg></div>
      <h3>Interior Design</h3>
      <p>Lorem ipsum dolor sit amet consectetur adipiscing elit praesent urna sem semper sit amet auctor</p>
    </div>
    <div class="svc">
      <div class="svc-icon"><svg width="36" height="36" viewBox="0 0 36 36" fill="none" stroke="var(--orange)" stroke-width="2"><rect x="7" y="7" width="22" height="22"/><path d="M7 15h22M15 15v14"/></svg></div>
      <h3>Exterior Design</h3>
      <p>Lorem ipsum dolor sit amet consectetur adipiscing elit praesent urna sem semper sit amet auctor</p>
    </div>
    <div class="svc">
      <div class="svc-icon"><svg width="36" height="36" viewBox="0 0 36 36" fill="none" stroke="var(--orange)" stroke-width="2"><path d="M6 28 22 12"/><path d="M20 8l8 8-4 4-8-8z"/><path d="M6 20h8v8"/></svg></div>
      <h3>Renovations</h3>
      <p>Lorem ipsum dolor sit amet consectetur adipiscing elit praesent urna sem semper sit amet auctor</p>
    </div>
    <div class="svc">
      <div class="svc-icon"><svg width="36" height="36" viewBox="0 0 36 36" fill="none" stroke="var(--orange)" stroke-width="2"><path d="M18 5l11 4v8c0 7-5 12-11 14-6-2-11-7-11-14V9z"/><path d="M13 18l4 4 6-7"/></svg></div>
      <h3>Safety management</h3>
      <p>Lorem ipsum dolor sit amet consectetur adipiscing elit praesent urna sem semper sit amet auctor</p>
    </div>
  </div>
</section>

<section class="about">
  <svg class="about-bg" width="1200" height="830" viewBox="0 0 1200 830">
    <polygon points="0,100 420,50 0,170" fill="var(--sky)"/>
    <polygon points="0,140 760,20 1200,70 1200,830 0,830" fill="var(--navy)"/>
  </svg>
  <div class="about-copy">
    <h2>Who We Are</h2>
    <p>Construction Company that specializes in Water and Fire Damage, Residential ReModels, Landscaping and Building ADU (Accessory Dwelling Unit)</p>
    <p>Growing and changing families often need additional space, and a remodeling project can often provide that. Adding a new area, or repurposing an existing one.</p>
    <ul class="ticks">
      <li><svg width="14" height="14" viewBox="0 0 14 14"><path d="M2 7l3 3 7-7" stroke="var(--orange)" stroke-width="2" fill="none"/></svg>We've reputation for excellence</li>
      <li><svg width="14" height="14" viewBox="0 0 14 14"><path d="M2 7l3 3 7-7" stroke="var(--orange)" stroke-width="2" fill="none"/></svg>Guided By Commitment</li>
      <li><svg width="14" height="14" viewBox="0 0 14 14"><path d="M2 7l3 3 7-7" stroke="var(--orange)" stroke-width="2" fill="none"/></svg>We build partnerships</li>
      <li><svg width="14" height="14" viewBox="0 0 14 14"><path d="M2 7l3 3 7-7" stroke="var(--orange)" stroke-width="2" fill="none"/></svg>A team of professionals</li>
    </ul>
    <span class="btn">Contact Now</span>
  </div>
  <div class="about-dots"></div>
  <div class="about-photo" role="img" aria-label="Worker in a hard hat installing siding on a house from a ladder"></div>
</section>

<section class="projects">
  <h2 class="sec-title">Recent Projects</h2>
  <div class="proj-grid">
    <div class="proj p1" role="img" aria-label="Flooded front yard of a house"><span>Water Damage</span></div>
    <div class="proj feature"><span>Fire Damage</span><p>Lorem ipsum dolor sit amet consectetur adipiscing elit praesent urna sem</p></div>
    <div class="proj p3" role="img" aria-label="Remodeled living room interior"><span>Residential Remodels</span></div>
    <div class="proj p4" role="img" aria-label="Gardener trimming a hedge"><span>Landscaping</span></div>
    <div class="proj p5" role="img" aria-label="Newly built accessory dwelling unit"><span>Building ADU</span></div>
    <div class="proj p6" role="img" aria-label="Bright restored interior with plants"><span>Water Damage</span></div>
  </div>
</section>

<section class="stats">
  <div class="stat"><div class="stat-num">53</div><div class="stat-label">Total Projects</div></div>
  <div class="stat"><div class="stat-num">371</div><div class="stat-label">Staff Members</div></div>
  <div class="stat"><div class="stat-num">15</div><div class="stat-label">Working in States</div></div>
  <div class="stat"><div class="stat-num">2,600</div><div class="stat-label">Hours For Work</div></div>
</section>

<section class="testimonials">
  <h2 class="sec-title">What People Say!</h2>
  <p class="sec-intro">Lorem ipsum dolor sit amet, consectetur adipiscing elit. Praesent urna sem, semper sit amet auctor in, auctor nisl leo. Curabitur aliquam sit amet turpis at.</p>
  <div class="quotes">
    <div class="quote">
      <div class="quote-box">"Summit Builders rebuilt our kitchen after a pipe burst and the whole team was careful, quick and honest from day one. We never had to chase anyone for updates and the result looks better than before."</div>
      <div class="person"><div class="avatar a1" role="img" aria-label="Portrait of a client"></div><div><h4>Evan Hale</h4><small>Homeowner</small></div></div>
    </div>
    <div class="quote">
      <div class="quote-box">"Summit Builders is one of the finest general contractors we have worked with. The crew planned our ADU with great care, kept the site clean and finished the project on time and within budget."</div>
      <div class="person"><div class="avatar a2" role="img" aria-label="Portrait of a client"></div><div><h4>Nora Patel</h4><small>Homeowner</small></div></div>
    </div>
  </div>
</section>

<section class="cta">
  <h2>We Deliver Landmark Projects</h2>
  <p>Discover ways to increase your home's value and stay on top of local trends</p>
  <div class="cta-form"><div class="field">Enter Your Email Address</div><div class="send">Submit</div></div>
</section>

<footer class="footer">
  <div class="foot-cols">
    <div class="foot-brand">
      <div class="brand"><span class="brand-mark"></span>Summit Builders</div>
      <p>Lorem ipsum is simply dummy text of the printing and typesetting industry. Lorem ipsum has been the industry's standard dummy text ever since the.</p>
      <div class="socials"><i></i><i></i><i></i><i></i></div>
    </div>
    <div class="col">
      <h4>Working Hours</h4>
      <p>we work 7 days a week, every day excluding major holidays. Contact us if you have an emergency, with our hotline and contact form.</p>
      <p style="margin-top:14px">monday – friday 10:00 – 16:00<br>saturday 12:00 – 17:00<br>sunday and holidays 09:00 – 12:00</p>
    </div>
    <div class="col">
      <h4>Contact us</h4>
      <p><b>Daniel R. Moss</b> | Branch Manager<br>Office : 555-010-4821<br>Direct : 555-010-7734 · Fax : 555-010-2290<br>dmoss@summitbuildersca.example<br>410 Ridgeview Ave, Fairhaven, CA 90000</p>
    </div>
  </div>
</footer>
<div class="copyright">Copyright © 2022 Summit Builders</div>

</body>
</html>
```